Business Card Design Project

I want a design for my business cards based on an excisting logo design.

Target Market(s)

Marketeers, PR-peeps, CEO's, decisionmakers, entrepreneurs

Industry/Entity Type

Business

Requirements
Nice to have
• Some visual interest on the back too
Should not have
• Sarif on the font

```html
<!DOCTYPE html>
<html lang="nl">
<head>
<meta charset="utf-8">
<title>LimeLeafPR – visitekaartjes</title>
<link rel="stylesheet" href="https://fonts.googleapis.com/css2?family=Roboto:wght@300;400;500&family=Roboto+Condensed:wght@400&display=swap">
<style>
  :root {
    --backdrop: #5f7680;
    --card: #2b2a29;
    --lime: #a6cb1c;
    --grey: #9a9a98;
    --grey-light: #b5b5b3;
  }
  * { margin: 0; padding: 0; box-sizing: border-box; }
  html, body { width: 1200px; height: 960px; overflow: hidden; }
  body {
    background: var(--backdrop);
    font-family: "Roboto", Arial, sans-serif;
    position: relative;
  }
  .card {
    position: absolute;
    left: 320px;
    width: 560px;
    height: 350px;
    background: var(--card);
    border-radius: 4px;
    box-shadow: 0 12px 30px rgba(0,0,0,.35);
    overflow: hidden;
  }
  .card--front { top: 100px; }
  .card--back { top: 510px; }

  .brand-mark {
    position: absolute;
    width: 130px; height: 130px;
    border-radius: 50%;
    background: var(--lime);
  }
  .brand-name {
    position: absolute;
    font-weight: 300;
    white-space: nowrap;
  }

  /* front */
  .card--front .brand-mark { left: 62px; top: 62px; }
  .card--front .brand-name {
    left: 38px; top: 228px;
    font-size: 36px;
    color: var(--grey);
  }
  .holder-name {
    position: absolute;
    left: 300px; top: 58px;
    font-family: "Roboto Condensed", Arial, sans-serif;
    font-weight: 400;
    font-size: 26px;
    color: var(--lime);
    letter-spacing: .5px;
  }
  .contact-list {
    position: absolute;
    left: 300px; top: 130px;
    list-style: none;
  }
  .contact-item {
    display: flex;
    align-items: center;
    height: 26px;
    font-size: 14.5px;
    font-weight: 300;
    color: var(--grey-light);
    white-space: nowrap;
  }
  .contact-item--web { font-weight: 500; }
  .contact-icon {
    width: 12px; height: 12px;
    margin-right: 14px;
    flex: none;
  }
  .contact-icon--social {
    background: var(--lime);
    border-radius: 2px;
  }

  /* back */
  .card--back .brand-mark { left: 215px; top: 60px; }
  .card--back .brand-name {
    left: 0; right: 0; top: 205px;
    text-align: center;
    color: var(--lime);
    font-size: 30px;
  }
  .tagline {
    position: absolute;
    left: 0; right: 0; bottom: 34px;
    text-align: center;
    font-size: 13px;
    color: var(--lime);
    letter-spacing: .6px;
    white-space: nowrap;
  }
</style>
</head>
<body>

<section class="card card--front" aria-label="Voorkant visitekaartje">
  <div class="brand-mark"></div>
  <div class="brand-name">LimeLeafPR</div>

  <h1 class="holder-name">LOTTE VERMEER</h1>
  <ul class="contact-list">
    <li class="contact-item">
      <svg class="contact-icon" viewBox="0 0 12 12" aria-hidden="true"><path fill="#a6cb1c" d="M1 3.5C1 2 2.5 1.5 6 1.5S11 2 11 3.5L9 4.5 8.3 3.3H3.7L3 4.5ZM3 5.5h6l1 5H2Z"/></svg>
      +31(0)6 20481937
    </li>
    <li class="contact-item">
      <svg class="contact-icon" viewBox="0 0 12 12" aria-hidden="true"><rect x="1" y="2.5" width="10" height="7.5" fill="#a6cb1c"/><path d="M1 2.5 6 7l5-4.5" fill="none" stroke="#2b2a29" stroke-width="1.2"/></svg>
      lotte.vermeer@limeleafpr.nl
    </li>
    <li class="contact-item">
      <svg class="contact-icon" viewBox="0 0 12 12" aria-hidden="true"><path fill="#a6cb1c" d="M6 .5a3.8 3.8 0 0 1 3.8 3.8C9.8 7 6 11.5 6 11.5S2.2 7 2.2 4.3A3.8 3.8 0 0 1 6 .5Z"/><circle cx="6" cy="4.3" r="1.4" fill="#2b2a29"/></svg>
      Bosrandlaan 12, 6711 AB Ede
    </li>
    <li class="contact-item">
      <span class="contact-icon contact-icon--social"></span>
      /limeleafpr
    </li>
    <li class="contact-item">
      <span class="contact-icon contact-icon--social"></span>
      /_limeleafpr
    </li>
    <li class="contact-item contact-item--web">
      <svg class="contact-icon" viewBox="0 0 12 12" aria-hidden="true"><circle cx="6" cy="6" r="5.2" fill="#a6cb1c"/><path d="M1 6h10M6 .8c-2.4 2.8-2.4 7.6 0 10.4M6 .8c2.4 2.8 2.4 7.6 0 10.4" fill="none" stroke="#2b2a29" stroke-width=".9"/></svg>
      limeleafpr.nl
    </li>
  </ul>
</section>

<section class="card card--back" aria-label="Achterkant visitekaartje">
  <div class="brand-mark"></div>
  <div class="brand-name">LimeLeafPR</div>
  <p class="tagline">Verbindend en doelgericht advies • voor pers, merk en communicatie</p>
</section>

</body>
</html>
```